larvosk.net

We are a IT Service for the valley. I want a clean website, with new Design, like animated pictures. We focus on IT. Give me your best design. What I'm looking for is eye catching. Works with Smart Phones, and iPad, Tab. Need a section for Submit a support tickets and Remote support. I'm looking for new ideals. I'm open mind, let me see what you guys can do.

Target Market(s)

My clients to see what service and products we have.

Industry/Entity Type

It Service

Requirements
Must have
• Able to submit a trouble tickets and works with Smart Phones, iPad, Tab.

```html
<!DOCTYPE html>
<html lang="en">
<head>
<meta charset="utf-8">
<title>Larvosk Technology</title>
<link rel="stylesheet" href="https://fonts.googleapis.com/css2?family=Open+Sans:wght@400;600;700&display=swap">
<style>
:root{
  --navy:#1a1f7a;
  --nav-bg:#dcdcf5;
  --band:#ebebeb;
  --text:#222;
  --muted:#555;
  --link:#4a6fb0;
  --card-title:#17207a;
  --icon:#3a7fb8;
  --quote:#7a7a7a;
  --accent:#4fb3f0;
  --arrow:#8a90d0;
}
*{box-sizing:border-box;margin:0;padding:0}
html,body{width:1091px;height:1200px;overflow:hidden;background:#fff}
body{position:relative;font-family:'Open Sans',Arial,sans-serif;color:var(--text)}
.brand{position:absolute;left:28px;top:84px;display:flex;align-items:center;gap:10px}
.brand-mark{width:26px;height:26px;background:var(--navy)}
.brand-name{font-size:24px;font-weight:700;color:var(--navy);letter-spacing:.5px}
.nav{position:absolute;left:497px;top:91px;display:flex;height:39px;background:var(--nav-bg);width:451px}
.nav a{display:flex;align-items:center;justify-content:center;font-size:14px;color:#111;text-decoration:none}
.nav a.active{background:linear-gradient(#2e3496,#141a6e);color:#c9ccf3;width:92px}
.nav .services{width:118px}.nav .products{width:118px}.nav .contact{width:123px}
.hero-band{position:absolute;left:0;top:140px;width:1091px;height:400px;background:var(--band)}
.hero{position:absolute;left:25px;top:0;width:1043px;height:350px;background:#fff;box-shadow:0 14px 18px -12px rgba(0,0,0,.35)}
.hero-text{position:absolute;left:68px;top:92px;width:450px;font-size:22.5px;line-height:26px;color:#1a1a1a}
.hero-photo{position:absolute;right:0;top:0;width:520px;height:350px;background:radial-gradient(ellipse at 60% 55%,#1b6fc4 0%,#3d8fd8 35%,#cfe2f3 70%,#fff 100%)}
.dots{position:absolute;left:525px;top:370px;display:flex;gap:5px}
.dots span{width:10px;height:10px;border-radius:50%;background:#8a8fd0;border:1px solid #bbb}
.dots span:last-child{background:#fff}
.features{position:absolute;left:25px;top:560px;display:flex;gap:20px}
.feature{position:relative;width:157px;height:156px;background:#fff;border:1px solid #c8c8c8;border-radius:3px;box-shadow:5px 5px 0 #5a5a5a;padding:0 13px}
.feature svg{display:block;margin:24px auto 12px}
.feature h3{font-size:13.5px;font-weight:400;color:var(--card-title);margin-bottom:3px;white-space:nowrap}
.feature p{font-size:10px;line-height:14.5px;color:#333}
.section-title{position:absolute;font-size:21px;font-weight:400;color:#222}
.products-title{left:27px;top:767px}
.service-title{left:532px;top:767px}
.tile{position:absolute;width:131px;height:112px;border:1px solid #ccc;background:#fff;padding:10px}
.tile .img{width:100%;height:100%;background:linear-gradient(#f4f4f4,#cfcfcf)}
.tile.more{display:flex;flex-direction:column;align-items:center;justify-content:center;line-height:18px}
.tile.more b{font-size:20px;font-weight:600;color:#333}
.tile.more span{font-size:17px;color:#777}
.service-list{position:absolute;left:532px;top:806px;list-style:none}
.service-list li{display:flex;align-items:center;gap:8px;font-size:12.5px;color:var(--link);height:21px;white-space:nowrap}
.service-list li.support-link{font-weight:600}
.support{position:absolute;left:783px;top:765px;width:285px;height:144px;background:linear-gradient(90deg,#e6eef4 0%,#dde6ec 55%,#c89a7a 100%)}
.support .label1{position:absolute;left:0;top:22px;font-size:26px;font-weight:700;color:#5aa0cc;letter-spacing:-.5px;line-height:1}
.support .label2{position:absolute;left:4px;top:54px;font-size:22px;color:#222;line-height:1}
.support .phone{position:absolute;left:0;top:110px;font-size:18px;font-weight:700;color:#333;line-height:1}
.quote{position:absolute;left:529px;top:940px;width:539px;height:118px;background:var(--quote);overflow:hidden}
.quote .clock{position:absolute;right:0;top:0;width:245px;height:118px;background:radial-gradient(circle at 70% 60%,#ddd 0%,#bbb 35%,#3a3a3a 70%,#222 100%)}
.quote .line1{position:absolute;left:28px;top:14px;font-size:23px;color:#fff;line-height:1}
.quote .line2{position:absolute;left:28px;top:38px;font-size:21px;color:#fff;line-height:1}
.quote .line2 em{font-style:normal;font-size:28px;color:var(--accent)}
.quote .btn{position:absolute;left:29px;top:74px;width:127px;height:32px;border-radius:4px;background:linear-gradient(#fafafa,#cfcfcf);color:#666;font-size:15px;display:flex;align-items:center;justify-content:center}
.footer{position:absolute;left:0;top:1085px;width:1091px;height:115px;background:var(--band);text-align:center;padding-top:47px;font-size:15px;color:var(--muted)}
</style>
</head>
<body>
<header>
  <div class="brand"><span class="brand-mark"></span><span class="brand-name">LARVOSK TECHNOLOGY</span></div>
  <nav class="nav">
    <a class="active" href="#">HOME</a>
    <a class="services" href="#">SERVICES</a>
    <a class="products" href="#">PRODUCTS</a>
    <a class="contact" href="#">CONTACT</a>
  </nav>
</header>

<section class="hero-band">
  <div class="hero">
    <p class="hero-text">Founded in 2004, Larvosk Technology focus on quality of their products, along with their customer service to ensure both lengthy uptimes while also minimiz-<br>ing downtime.</p>
    <div class="hero-photo" role="img" aria-label="Photo of a coiled blue network cable with connector"></div>
  </div>
  <div class="dots"><span></span><span></span><span></span></div>
</section>

<section class="features">
  <div class="feature">
    <svg width="42" height="42" viewBox="0 0 42 42"><rect x="2" y="2" width="38" height="38" rx="2" fill="none" stroke="var(--icon)" stroke-width="3"/><path d="M12 28l10-14 8 12" fill="none" stroke="var(--icon)" stroke-width="2"/></svg>
    <h3>ACCESSIBILITY</h3><p>On-Call and ready to serve your needs. Service is only a phone call away.</p>
  </div>
  <div class="feature">
    <svg width="42" height="42" viewBox="0 0 42 42"><rect x="2" y="2" width="38" height="38" rx="2" fill="none" stroke="var(--icon)" stroke-width="3"/><rect x="11" y="11" width="20" height="14" fill="none" stroke="var(--icon)" stroke-width="2"/><path d="M9 30h24" stroke="var(--icon)" stroke-width="2"/></svg>
    <h3>QUALITY PRODUCTS</h3><p>Provide hardware or software that will suit your specific needs.</p>
  </div>
  <div class="feature">
    <svg width="42" height="42" viewBox="0 0 42 42"><rect x="2" y="2" width="38" height="38" rx="2" fill="none" stroke="var(--icon)" stroke-width="3"/><rect x="11" y="10" width="20" height="12" rx="2" fill="none" stroke="var(--icon)" stroke-width="2"/><circle cx="21" cy="28" r="4" fill="none" stroke="var(--icon)" stroke-width="2"/></svg>
    <h3>CONSULTATION</h3><p>We consult you on proper upgrades or purchases for your company.</p>
  </div>
  <div class="feature">
    <svg width="42" height="42" viewBox="0 0 42 42"><rect x="2" y="2" width="38" height="38" rx="2" fill="none" stroke="var(--icon)" stroke-width="3"/><circle cx="21" cy="21" r="10" fill="none" stroke="var(--icon)" stroke-width="2"/><path d="M21 15v6h5" fill="none" stroke="var(--icon)" stroke-width="2"/></svg>
    <h3>TURN AROUND TIME</h3><p>We Fix your network problem in a timely manner.</p>
  </div>
  <div class="feature">
    <svg width="42" height="42" viewBox="0 0 42 42"><rect x="2" y="2" width="38" height="38" rx="2" fill="none" stroke="var(--icon)" stroke-width="3"/><path d="M10 28h22" stroke="var(--icon)" stroke-width="2" stroke-dasharray="3 2"/><path d="M24 10l8 8M32 10l-8 8" stroke="var(--navy)" stroke-width="2"/></svg>
    <h3>LONGEVITY</h3><p>Building a long-term, trusting, relationship is our goal.</p>
  </div>
  <div class="feature">
    <svg width="42" height="42" viewBox="0 0 42 42"><rect x="2" y="2" width="38" height="38" rx="2" fill="none" stroke="var(--icon)" stroke-width="3"/><rect x="10" y="18" width="8" height="12" fill="none" stroke="var(--icon)" stroke-width="2"/><rect x="21" y="11" width="10" height="19" fill="none" stroke="var(--icon)" stroke-width="2"/></svg>
    <h3>TROUBLESHOOTING</h3><p>We will solve your network problems with a friendly smile.</p>
  </div>
</section>

<h2 class="section-title products-title">Products</h2>
<div class="tile" style="left:25px;top:811px"><div class="img" role="img" aria-label="Photo of a wide-format printer"></div></div>
<div class="tile" style="left:175px;top:811px"><div class="img" role="img" aria-label="Photo of an office desk phone"></div></div>
<div class="tile" style="left:325px;top:811px"><div class="img" role="img" aria-label="Photo of a software disc"></div></div>
<div class="tile" style="left:25px;top:946px"><div class="img" role="img" aria-label="Photo of a tower server"></div></div>
<div class="tile" style="left:175px;top:946px"><div class="img" role="img" aria-label="Photo of a desktop workstation with monitor"></div></div>
<div class="tile more" style="left:325px;top:946px"><b>VIEW</b><span>more</span></div>

<h2 class="section-title service-title">Service List</h2>
<ul class="service-list">
  <li><svg width="13" height="10" viewBox="0 0 13 10"><path d="M1 5h10M7 1l4 4-4 4" fill="none" stroke="var(--arrow)" stroke-width="1.6"/></svg>Halvern VOIP Phones</li>
  <li><svg width="13" height="10" viewBox="0 0 13 10"><path d="M1 5h10M7 1l4 4-4 4" fill="none" stroke="var(--arrow)" stroke-width="1.6"/></svg>Vantor Server</li>
  <li><svg width="13" height="10" viewBox="0 0 13 10"><path d="M1 5h10M7 1l4 4-4 4" fill="none" stroke="var(--arrow)" stroke-width="1.6"/></svg>Vantor Workstation</li>
  <li><svg width="13" height="10" viewBox="0 0 13 10"><path d="M1 5h10M7 1l4 4-4 4" fill="none" stroke="var(--arrow)" stroke-width="1.6"/></svg>Web Design</li>
  <li class="support-link"><svg width="13" height="10" viewBox="0 0 13 10"><path d="M1 5h10M7 1l4 4-4 4" fill="none" stroke="var(--arrow)" stroke-width="1.6"/></svg>Submit a Support Ticket</li>
  <li class="support-link"><svg width="13" height="10" viewBox="0 0 13 10"><path d="M1 5h10M7 1l4 4-4 4" fill="none" stroke="var(--arrow)" stroke-width="1.6"/></svg>Remote Support</li>
</ul>

<div class="support" role="img" aria-label="Technical support banner with a support agent wearing a headset">
  <span class="label1">TECHNICAL</span>
  <span class="label2">SUPPORT</span>
  <span class="phone">555-014-2273</span>
</div>

<div class="quote">
  <div class="clock" role="img" aria-label="Photo of a wall clock face"></div>
  <span class="line1">Get a</span>
  <span class="line2">Quote <em>TODAY</em></span>
  <span class="btn">CLICK HERE</span>
</div>

<footer class="footer">Larvosk Technology © 2012 | Terms of Service - Privacy Policy - Program Policies</footer>
</body>
</html>
```